Corporate Letterhead

Looking for a new corporate letterhead design. Our colors are orange and gray.

We'd like it if the below could be included somehow in the letterhead.                                       

Partnerships | Results | Quality

• Logo, Company Name, Address, Phone #, Fax #, Web address, Email address (optional), the phrase "A Service Disable Veteran Owned Small Business".

```html
<!DOCTYPE html>
<html lang="en">
<head>
<meta charset="utf-8">
<title>Vantara Systems, Inc — Letterhead</title>
<link rel="stylesheet" href="https://fonts.googleapis.com/css2?family=Arimo:wght@400;700&family=Open+Sans:wght@600&display=swap">
<style>
  :root {
    --backdrop: #000000;
    --paper: #ffffff;
    --brand-orange: #f7941d;
    --brand-gray: #9b9b9d;
    --rule: #58595b;
    --ink: #111111;
    --on-band: #ffffff;
  }
  * { box-sizing: border-box; margin: 0; padding: 0; }
  html, body {
    width: 1200px; height: 1200px; overflow: hidden;
    background: var(--backdrop);
  }
  .letterhead {
    position: absolute;
    left: 244px; top: 97px;
    width: 715px; height: 1009px;
    background: var(--paper);
  }
  .brand {
    position: absolute;
    left: 104px; top: 50px;
    display: flex; align-items: center; gap: 26px;
  }
  .brand-mark {
    width: 92px; height: 92px; border-radius: 50%;
    background: var(--brand-orange);
  }
  .brand-name {
    font-family: "Arimo", Arial, sans-serif;
    font-weight: 700;
    color: var(--brand-orange);
    line-height: 1;
  }
  .brand-name .primary { display: block; font-size: 56px; letter-spacing: 2px; }
  .brand-name .secondary { display: block; font-size: 27px; letter-spacing: 3px; margin-top: 6px; }
  .header-rule {
    position: absolute;
    left: 0; top: 164px;
    width: 494px; height: 1.5px;
    background: var(--rule);
  }
  .tagline {
    position: absolute;
    left: 502px; top: 155px;
    font-family: "Open Sans", Arial, sans-serif;
    font-weight: 600; font-size: 12.5px;
    color: var(--ink);
    white-space: nowrap;
  }
  .footer-band {
    position: absolute;
    left: 8px; top: 958px;
    width: 700px; height: 45px;
    display: flex;
    font-family: "Arimo", Arial, sans-serif;
    color: var(--on-band);
  }
  .office-label {
    width: 107px;
    background: var(--brand-orange);
    font-weight: 700; font-size: 15px; line-height: 17px;
    text-align: right;
    padding: 6px 7px 0 0;
    letter-spacing: 0.5px;
  }
  .office-address {
    flex: 1;
    background: var(--brand-gray);
    font-size: 14px; line-height: 17px;
    text-align: center;
    padding-top: 5px;
    letter-spacing: 0.4px;
  }
</style>
</head>
<body>
  <main class="letterhead">
    <header>
      <div class="brand">
        <div class="brand-mark"></div>
        <div class="brand-name">
          <span class="primary">VANTARA</span>
          <span class="secondary">SYSTEMS, INC</span>
        </div>
      </div>
      <div class="header-rule"></div>
      <p class="tagline">Partnerships | Results | Quality</p>
    </header>
    <footer class="footer-band">
      <div class="office-label">Corporate<br>Office:</div>
      <div class="office-address">
        18 Harbor Tech Drive | Westbrook Innovation Park II<br>
        #03-12/14 | The Lyra | Westbrook 204538
      </div>
    </footer>
  </main>
</body>
</html>
```